Webdesign für Personalvermittlung
Zielgruppe
Personalvermittlung
Aufgabenstellung
es soll einladend - nicht zu überladen und natürlich cool und modern sein

```html
<!DOCTYPE html>
<html lang="de">
<head>
<meta charset="utf-8">
<title>sorgsam job – Über Uns</title>
<link href="https://fonts.googleapis.com/css2?family=Raleway:ital,wght@0,400;0,500;0,600;0,700;0,800;1,300;1,400;1,500;1,600;1,700&family=Poppins:wght@400;500;600&display=swap" rel="stylesheet">
<style>
:root{
  --blue:#2aa7df;
  --orange:#f7902a;
  --light:#d5edf8;
  --ink:#2b2b2b;
  --muted:#6a6a6a;
  --dark:#1f1d2b;
  --line:#2f8fd0;
  --white:#ffffff;
}
*{box-sizing:border-box;margin:0;padding:0}
html,body{width:1200px;height:3248px;overflow:hidden;background:var(--white)}
body{position:relative;font-family:"Raleway",sans-serif;color:var(--ink)}
.abs{position:absolute}

/* header */
.brand{left:83px;top:14px;width:130px;text-align:center}
.brand-dot{width:46px;height:46px;border-radius:50%;background:var(--blue);margin:0 auto 6px}
.brand-name{font-family:"Poppins",sans-serif;font-weight:500;font-size:17px;color:#333}
.top-ask{left:649px;top:41px;font-family:"Poppins",sans-serif;font-size:11px;color:#333}
.top-phone{left:800px;top:38px;font-family:"Poppins",sans-serif;font-size:13px;font-weight:600;color:var(--blue);display:flex;gap:6px;align-items:center}
.apply{left:966px;top:30px;width:152px;height:38px;border-radius:4px;background:var(--orange);color:var(--white);font-family:"Poppins",sans-serif;font-weight:500;font-size:16px;display:flex;align-items:center;justify-content:center;gap:8px}

.nav{left:0;top:108px;width:1200px;height:61px;background:var(--blue)}
.nav a{position:absolute;top:0;height:61px;line-height:61px;color:var(--white);font-weight:600;font-size:20px;text-decoration:none;transform:translateX(-50%)}
.nav a.active{background:var(--orange);width:154px;text-align:center}

/* hero */
.hero{left:49px;top:198px;width:1101px;height:637px;border-radius:12px;overflow:hidden;background:linear-gradient(135deg,#5b6a78,#3c4754 50%,#6b6f7a);box-shadow:0 2px 8px rgba(0,0,0,.3)}
.hero-inner{position:absolute;inset:0;background:rgba(40,40,55,.45);color:var(--white);text-align:center}
.hero h1{position:absolute;top:42px;width:100%;font-size:36px;font-weight:600}
.hero .rule{position:absolute;left:223px;top:99px;width:624px;height:2px;background:var(--line)}
.hero .tag{position:absolute;top:120px;width:100%;font-style:italic;font-weight:600;font-size:20px}
.hero .copy{position:absolute;left:95px;top:197px;width:880px;font-style:italic;font-size:20px;line-height:26px}
.hero .copy p{margin-bottom:26px}
.stats{position:absolute;top:528px;left:0;width:100%;height:80px}
.stat{position:absolute;display:flex;align-items:center;gap:12px}
.stat b{font-family:"Poppins",sans-serif;font-weight:600;font-size:76px;line-height:1}
.stat span{font-style:italic;font-weight:500;font-size:20px;text-align:left;line-height:28px}
.divider{position:absolute;top:0;width:5px;height:76px;background:var(--white)}

/* vision */
.vision{left:0;top:905px;width:1200px;height:466px;background:var(--light)}
.vision h2{position:absolute;left:83px;top:92px;font-size:34px;font-weight:600;color:var(--orange)}
.vision .rule{position:absolute;left:83px;top:155px;width:406px;height:2px;background:var(--line)}
.vision p{position:absolute;left:87px;top:192px;width:460px;font-style:italic;font-weight:300;font-size:20px;line-height:26.5px;color:#444}
.country{left:690px;top:-4px;width:340px;height:490px;background:#b9c3cd;border-radius:42% 38% 46% 40%/30% 36% 40% 44%}

/* team */
.sec-title{width:1200px;text-align:center;font-weight:600;font-size:34px}
.sec-rule{height:2px;background:var(--line)}
.sec-tag{width:1150px;text-align:center;font-style:italic;font-weight:500;font-size:20px}
.member{width:228px;text-align:center}
.member .photo{height:207px;border-radius:10px;background:linear-gradient(160deg,#c9d3dc,#7f8b98)}
.member .role{margin-top:14px;font-style:italic;font-size:14px;color:#333}
.member .name{margin-top:4px;font-style:italic;font-weight:700;font-size:17px}
.arrow{width:44px;height:44px;border-radius:50%;background:var(--blue);display:flex;align-items:center;justify-content:center}

/* contact */
.form-title{left:112px;top:1890px;width:560px;font-size:30px;font-weight:700;color:var(--orange);line-height:38px}
.form-rule{left:112px;top:1978px;width:88px;height:2px;background:var(--line)}
.form-sub{left:112px;top:1994px;width:553px;font-style:italic;font-size:14px;color:#777;border-bottom:1px solid #f3d3b3;padding-bottom:4px}
.lbl{font-style:italic;font-size:14px;color:#222}
.field{border:1px solid #e2e2e2;font-style:italic;font-size:13px;color:#999;padding:14px}
.field.focus{border-color:#2f6ed0}
.send{left:112px;top:2381px;width:553px;height:51px;background:var(--orange);color:var(--white);font-family:"Poppins",sans-serif;font-weight:600;font-size:17px;display:flex;align-items:center;justify-content:center}

.card{left:702px;top:1865px;width:498px;height:642px;background:var(--light);border-radius:16px 0 0 16px;overflow:hidden}
.card h2{position:absolute;left:18px;top:30px;font-size:35px;font-weight:700;color:var(--orange)}
.card .h3{position:absolute;left:18px;font-style:italic;font-size:28px;color:#333}
.avatar{position:absolute;left:18px;top:130px;width:141px;height:138px;border-radius:50%;background:linear-gradient(160deg,#c9d3dc,#6e7a87)}
.card .person{position:absolute;left:25px;top:286px;font-style:italic;font-weight:700;font-size:28px}
.row{position:absolute;left:25px;display:flex;align-items:center;gap:14px;font-style:italic;font-weight:700;font-size:17px}
.row a{color:var(--ink)}
.corner{position:absolute;right:-87px;bottom:-87px;width:174px;height:174px;border-radius:50%;background:var(--orange)}

.map{left:14px;top:2543px;width:1186px;height:393px;background:linear-gradient(135deg,#e8ebef,#dfe6e2 60%,#eee7d6)}

/* footer */
.footer{left:0;top:2989px;width:1200px;height:214px;background:var(--dark);color:var(--white)}
.f-brand{position:absolute;left:112px;top:20px;width:200px;text-align:center}
.f-dot{width:74px;height:74px;border-radius:50%;background:var(--blue);margin:0 auto 10px}
.f-brand .n{font-family:"Poppins",sans-serif;font-weight:500;font-size:27px}
.socials{position:absolute;left:133px;top:152px;display:flex;gap:12px}
.socials i{display:block;width:24px;height:24px;background:var(--white);border-radius:3px}
.f-head{position:absolute;top:12px;font-style:italic;font-size:20px;color:#ddd}
.f-rule{position:absolute;top:50px;width:66px;height:2px;background:var(--orange)}
.f-list{position:absolute;left:447px;top:84px;list-style:none;font-style:italic;font-size:13px;color:#ccc;line-height:19px}
.f-list li::before{content:"• ";}
.sub-box{position:absolute;left:803px;top:72px;width:329px;height:49px;background:var(--white);display:flex;align-items:center;gap:12px;padding-left:16px;font-size:13px;color:#888}
.sub-box .sep{width:1px;height:22px;background:#ccc}
.sub-note{position:absolute;left:803px;top:138px;width:320px;font-style:italic;font-size:13px;line-height:19px;color:#ccc}
.copyright{left:0;top:3222px;width:1208px;text-align:center;font-family:"Poppins",sans-serif;font-size:14px;color:#2b3a6b}
</style>
</head>
<body>

<header>
  <div class="abs brand"><div class="brand-dot"></div><div class="brand-name">sorgsam job</div></div>
  <div class="abs top-ask">Any Qirgendeine Frage</div>
  <div class="abs top-phone">
    <svg width="14" height="14" viewBox="0 0 24 24"><path d="M6.6 10.8a15 15 0 006.6 6.6l2.2-2.2c.3-.3.7-.4 1-.2 1.1.4 2.3.6 3.6.6.6 0 1 .4 1 1V20c0 .6-.4 1-1 1A17 17 0 013 4c0-.6.4-1 1-1h3.5c.6 0 1 .4 1 1 0 1.3.2 2.5.6 3.6.1.3 0 .7-.2 1z" fill="#2aa7df"/></svg>
    07231 555 019 2
  </div>
  <div class="abs apply">
    <svg width="16" height="16" viewBox="0 0 24 24"><path d="M4 20h4L19 9l-4-4L4 16z M3 22h18" stroke="#fff" stroke-width="2" fill="none"/></svg>
    ANWENDEN
  </div>
  <nav class="abs nav">
    <a style="left:159px">Home</a>
    <a style="left:364px">Wir Bieten Dir</a>
    <a class="active" style="left:587px">Uber Uns</a>
    <a style="left:803px">Kontakt</a>
  </nav>
</header>

<section class="abs hero" role="img" aria-label="Gruppenfoto eines Pflegeteams im Krankenhausflur">
  <div class="hero-inner">
    <h1>Uber Uns</h1>
    <div class="rule"></div>
    <div class="tag">Ihr Erfolg, unser Engagement</div>
    <div class="copy">
      <p>Mit mehr als 15 Jahren Erfahrung in der Vermittlung von Fach- und Führungskräften, steht Ihnen das Team von sorgsam-job.de als vertrauensvoller Partner bei Ihrem Jobwechsel zur Seite.</p>
      <p>Gemeinsam finden wir die ideale Stelle, welche auf Grund Ihrer persönlichen Wünsche und Vorstellungen am besten zu Ihnen passt.</p>
      <p>Lehnen Sie sich bequem zurück und überlassen das Finden Ihres neuen Arbeitsplatzes uns.</p>
      <p>Am Ende des Tages entscheiden Sie, ob ein Vorstellungsgespräch stattfinden soll oder wir für Sie weitersuchen!</p>
    </div>
    <div class="stats">
      <div class="stat" style="left:148px"><b>15</b><span>Jahren<br>Erfahrung</span></div>
      <div class="divider" style="left:367px"></div>
      <div class="stat" style="left:400px"><b>100+</b><span>Mitglied</span></div>
      <div class="divider" style="left:690px"></div>
      <div class="stat" style="left:713px"><b>10+</b><span>Arbeitsplatz</span></div>
    </div>
  </div>
</section>

<section class="abs vision">
  <h2>Unsere Vision</h2>
  <div class="rule"></div>
  <p>SORGSAM-JOB.de hat es sich mit über 15 Jahren Erfahrung zum Ziel gesetzt, Fachkräften im Gesundheitswesen dabei zu helfen, lohnende Führungspositionen zu finden. Wir sind darauf spezialisiert, qualifizierte Kandidaten mit erstklassigen Gesundheitseinrichtungen zusammenzubringen.</p>
  <div class="abs country" role="img" aria-label="Landkarte von Deutschland"></div>
</section>

<section class="team">
  <h2 class="abs sec-title" style="left:0;top:1402px">Unser Team</h2>
  <div class="abs sec-rule" style="left:260px;top:1458px;width:623px"></div>
  <div class="abs sec-tag" style="left:0;top:1480px">Ihr Erfolg, unser Engagement</div>

  <div class="abs arrow" style="left:59px;top:1635px"><svg width="14" height="14" viewBox="0 0 14 14"><path d="M9 2L4 7l5 5" stroke="#fff" stroke-width="2" fill="none"/></svg></div>
  <div class="abs arrow" style="left:1087px;top:1635px"><svg width="14" height="14" viewBox="0 0 14 14"><path d="M5 2l5 5-5 5" stroke="#fff" stroke-width="2" fill="none"/></svg></div>

  <div class="abs member" style="left:112px;top:1555px"><div class="photo" role="img" aria-label="Porträt eines Mannes im Anzug"></div><div class="role">Ansprechpartner</div><div class="name">Herr Matthias Kerber</div></div>
  <div class="abs member" style="left:358px;top:1555px"><div class="photo" role="img" aria-label="Porträt einer Ärztin mit Globus"></div><div class="role">CEO</div><div class="name">Herr Matthias Kerber</div></div>
  <div class="abs member" style="left:604px;top:1551px"><div class="photo" role="img" aria-label="Laborarbeit mit Mikroskop"></div><div class="role">Analyse</div><div class="name">Herr Matthias Kerber</div></div>
  <div class="abs member" style="left:849px;top:1555px"><div class="photo" role="img" aria-label="Porträt eines Mannes mit Notizblock"></div><div class="role">Pflegedienstleiter/In</div><div class="name">Herr Matthias Kerber</div></div>
</section>

<section class="contact">
  <h2 class="abs form-title">Nimm ganz einfach Kontakt zu uns auf:</h2>
  <div class="abs form-rule"></div>
  <div class="abs form-sub">ich möchte einen Rückruf und ein persönliches Erstgespräch</div>

  <div class="abs lbl" style="left:112px;top:2056px">Nachname</div>
  <div class="abs field" style="left:112px;top:2080px;width:263px;height:44px">Gib deinen Namen ein</div>
  <div class="abs lbl" style="left:402px;top:2056px">E-Mail-Adresse</div>
  <div class="abs field focus" style="left:402px;top:2080px;width:263px;height:44px">John.exp@gm|</div>
  <div class="abs lbl" style="left:112px;top:2143px">Betreff</div>
  <div class="abs field" style="left:112px;top:2167px;width:553px;height:70px">Geben Sie Ihre Anforderung ein...</div>
  <div class="abs lbl" style="left:112px;top:2254px">Nachricht</div>
  <div class="abs field" style="left:112px;top:2278px;width:553px;height:69px">Was möchten Sie vermitteln?</div>
  <div class="abs send">SENDEN</div>

  <aside class="abs card">
    <h2>KONTAKTDATEN</h2>
    <div class="h3" style="top:80px">Ansprechpartner</div>
    <div class="avatar" role="img" aria-label="Porträt des Ansprechpartners"></div>
    <div class="person">Herr Matthias Kerber</div>
    <div class="row" style="top:335px">
      <svg width="22" height="22" viewBox="0 0 24 24"><path d="M6.6 10.8a15 15 0 006.6 6.6l2.2-2.2c.3-.3.7-.4 1-.2 1.1.4 2.3.6 3.6.6.6 0 1 .4 1 1V20c0 .6-.4 1-1 1A17 17 0 013 4c0-.6.4-1 1-1h3.5c.6 0 1 .4 1 1 0 1.3.2 2.5.6 3.6.1.3 0 .7-.2 1z" fill="#f7902a"/></svg>
      07231 555 019 2</div>
    <div class="row" style="top:380px">
      <svg width="24" height="24" viewBox="0 0 24 24"><rect x="2" y="4" width="20" height="16" rx="3" fill="#f7902a"/><path d="M5 8l7 5 7-5" stroke="#fff" stroke-width="2" fill="none"/></svg>
      <a>matthias.kerber@sorgsam-job.de</a></div>
    <div class="h3" style="top:430px">Adresse:</div>
    <div class="row" style="top:488px;align-items:flex-start;width:340px;line-height:20px">
      <svg width="26" height="26" viewBox="0 0 24 24" style="flex:none"><path d="M12 2a6 6 0 00-6 6c0 4.5 6 12 6 12s6-7.5 6-12a6 6 0 00-6-6z" fill="#f7902a"/><circle cx="12" cy="8" r="2.2" fill="#fff"/></svg>
      Lindenhof 12, 76530 Musterstadt</div>
    <div class="row" style="top:538px">
      <svg width="22" height="22" viewBox="0 0 24 24"><path d="M6.6 10.8a15 15 0 006.6 6.6l2.2-2.2c.3-.3.7-.4 1-.2 1.1.4 2.3.6 3.6.6.6 0 1 .4 1 1V20c0 .6-.4 1-1 1A17 17 0 013 4c0-.6.4-1 1-1h3.5c.6 0 1 .4 1 1 0 1.3.2 2.5.6 3.6.1.3 0 .7-.2 1z" fill="#f7902a"/></svg>
      07231 555 019 2</div>
    <div class="row" style="top:584px">
      <svg width="24" height="24" viewBox="0 0 24 24"><rect x="2" y="4" width="20" height="16" rx="3" fill="#f7902a"/><path d="M5 8l7 5 7-5" stroke="#fff" stroke-width="2" fill="none"/></svg>
      <a>info@sorgsam-job.de</a></div>
    <div class="corner"></div>
  </aside>
</section>

<div class="abs map" role="img" aria-label="Stadtplan mit Standortmarkierung des Büros"></div>

<footer class="abs footer">
  <div class="f-brand"><div class="f-dot"></div><div class="n">sorgsam job</div></div>
  <div class="socials"><i></i><i></i><i></i><i></i></div>
  <div class="f-head" style="left:437px">Seitenverzeichnis</div>
  <div class="f-rule" style="left:437px"></div>
  <ul class="f-list"><li>HOME</li><li>WIR BIETEN DIR</li><li>ÜBER UNS</li><li>KONTAKT</li></ul>
  <div class="f-head" style="left:803px">Abonnieren</div>
  <div class="f-rule" style="left:803px"></div>
  <div class="sub-box">
    <svg width="18" height="18" viewBox="0 0 24 24"><rect x="3" y="5" width="18" height="14" rx="3" stroke="#f7902a" stroke-width="2" fill="none"/><path d="M7 9l5 4 5-4" stroke="#f7902a" stroke-width="2" fill="none"/></svg>
    <span class="sep"></span>Geben sie ihre E-Mail Adresse ein
  </div>
  <p class="sub-note">Senden Sie eine E-Mail und Sie erhalten regelmäßig unsere Newsletter, Service-Blogs und Pressemitteilungen</p>
</footer>
<div class="abs copyright">Copyright 2024 sorgsam-job.de, All Right Reserved</div>

</body>
</html>
```